Web re-design project www.vempresoft.com

We need a corporate website for a startup company called Vempre Labs. The company offers web-based worksite management system for big construction companies. In short, replacing annoying papers with iPads.
We need the site main page to provide basic overview of the company and then inner page layout for displaying news and detailed information about products.
Currently we have a site up at:
http://www.vempresoft.com/en/main
but as you can see the graphic design is a bit lacking in quality(implemented by a tech guy :)
We need you to pimp that web site design up!
There is possibility for more freelance work in the future related to our web products, slide show designs and printed marketing materials.
Our main product is LOMVI. You can find a short presentation about what it does here:
http://www.vempresoft.com/en/lomvi
Here you can find packages of images and screenshots related to our company:
https://files.plimbox.net/u/7719026/vempre_images.zip
https://files.plimbox.net/u/7719026/vempresoft%20images2.zip
Product logo svg can be found here:
https://files.plimbox.net/u/7719026/LOMVI-logo.svg
Your are not forced to use those images, but hopefully there will be something that is useful.
Hope to hear from you guys soon!
Cheers,
Ossi
Update:
We will be using LOMVI logo as the company brand. I don't like our current Vempre Labs company logo, so that doesn't need to be included in the site design.
Update 2:
I like website designs that are "light", elegant and pretty simplistic. One example is our product login page (screenshot included in files).
Update 3:
Sites from the same industry / type of products:
http://www.rakmoda.fi/
http://www.quarvelgrid.com/products/software/network-applications/fieldsync-3d
http://www.dornvex.com/construction/heavy-civil/software-solutions/Linked-Network.aspx?dtID=overview&
Target audience for the website is companies in the construction sector, and possibly corporate investors
Graphic Design

```html
<!DOCTYPE html>
<html lang="en">
<head>
<meta charset="utf-8">
<title>LOMVI – Vempre Labs</title>
<link href="https://fonts.googleapis.com/css2?family=Ubuntu:wght@400;500;700&family=Play:wght@400;700&display=swap" rel="stylesheet">
<style>
:root{
  --red:#e30613;
  --red-dark:#b5000b;
  --ink:#222;
  --grey-text:#555;
  --heading:#4a4a4a;
  --line:#cfcfcf;
  --nav-top:#3a3a3a;
  --nav-bottom:#0e0e0e;
  --footer:#3b3b3b;
  --page-top:#eef3f7;
}
*{margin:0;padding:0;box-sizing:border-box}
html,body{width:1108px;height:1200px;overflow:hidden;background:#fff}
body{font-family:"Ubuntu",sans-serif;color:var(--ink)}
.stage{position:relative;width:1200px;height:1300px;transform:scale(0.9233);transform-origin:0 0;
  background:linear-gradient(180deg,var(--page-top) 0,#fafcfd 300px,#f4f7f9 567px,#fff 567px)}
.abs{position:absolute}

/* header */
.logo{left:120px;top:12px;width:310px;height:91px;background:#fff;display:flex;align-items:center;gap:18px;padding-left:6px}
.logo-mark{width:46px;height:46px;border-radius:50%;background:var(--red)}
.logo-name{font-family:"Ubuntu",sans-serif;font-weight:500;font-size:58px;color:#1a1a1a;letter-spacing:1px}
.contact{right:122px;top:30px;display:flex;align-items:center;gap:5px;font-size:11px;color:#222}
.contact .sep{color:#999;margin:0 6px}
.contact .signup{color:var(--red);font-weight:700}
.search{left:830px;top:67px;width:250px;height:32px;border:1px solid #c8c8c8;border-radius:3px;background:#fff;display:flex}
.search span{flex:1;font-size:11px;color:#999;padding:10px 9px}
.search i{width:34px;border-left:1px solid #ccc;background:linear-gradient(#fafafa,#e4e4e4);display:flex;align-items:center;justify-content:center}

/* nav */
.nav{left:120px;top:118px;width:960px;height:48px;border-radius:5px 5px 3px 3px;overflow:hidden;background:linear-gradient(var(--nav-top),var(--nav-bottom) 39px,var(--red) 39px,var(--red))}
.nav ul{list-style:none;display:flex;align-items:center;height:39px;padding-left:36px}
.nav li{font-family:"Play",sans-serif;font-size:14px;color:#fff;text-transform:uppercase}
.nav li.sep{color:#ddd;margin:0 0}
.nav li.item{padding:0 29px}
.nav li.active{background:var(--red);height:30px;margin-top:9px;line-height:29px;padding:0 18px;border-radius:3px 3px 0 0;margin-right:12px}

/* hero */
.hero{left:120px;top:174px;width:960px;height:393px;border-radius:6px 6px 0 0;overflow:hidden}
.hero-photo{position:absolute;inset:0;background:radial-gradient(ellipse at 60% 45%,#c7a294 0,#8a8f9a 28%,#3a3f48 55%,#2a2c33 70%,#c9ccd3 100%)}
.hero-panel{position:absolute;left:35px;top:0;width:324px;height:393px;background:rgba(214,214,218,.93);padding:38px 10px 0 11px}
.hero-panel h1{font-family:"Ubuntu",sans-serif;font-weight:400;font-size:22px;color:var(--red);margin-bottom:10px}
.hero-panel p{font-family:Arial,sans-serif;font-size:14px;line-height:20px;color:#222;margin-bottom:20px}
.hero-left{position:absolute;left:0;top:0;width:35px;height:393px;background:linear-gradient(90deg,#1f2228,#6d7a3a)}
.dots{position:absolute;left:430px;top:358px;width:100px;height:35px;background:#fff;border-radius:5px 5px 0 0;display:flex;justify-content:center;align-items:center;gap:10px}
.dots b{width:12px;height:12px;border-radius:50%;background:#222}
.dots b.on{background:var(--red)}

/* about */
.about{left:123px;top:604px;width:545px}
.section-title{font-family:"Play",sans-serif;font-weight:700;color:var(--heading)}
.about h2{font-size:29px;margin-bottom:14px}
.about p{font-size:11.6px;line-height:18px;color:var(--grey-text);margin-bottom:36px}
.btn{display:inline-flex;align-items:center;background:linear-gradient(#3a3a3a,#0d0d0d);color:#fff;font-family:"Ubuntu",sans-serif;font-weight:500;font-size:12px;border-radius:3px;box-shadow:0 1px 2px rgba(0,0,0,.4)}
.read-more{left:122px;top:918px;width:149px;height:35px;padding-left:19px;gap:28px}
.play{width:17px;height:17px;border-radius:50%;background:#fff;display:flex;align-items:center;justify-content:center}
.divider{left:681px;top:610px;width:1px;height:343px;background:var(--line)}

/* news */
.news{left:700px;top:604px;width:360px}
.news h2{font-size:23px;margin-bottom:6px}
.news-item h3{font-family:"Play",sans-serif;font-weight:400;font-size:19px;color:#4a4a4a;margin-left:1px}
.news-item h3 small{font-family:"Ubuntu",sans-serif;font-size:13px;color:var(--red)}
.news-row{display:flex;gap:4px;margin-top:10px;margin-left:-3px}
.thumb{width:126px;height:82px;background:#ddd;padding:5px;flex-shrink:0}
.thumb div{width:100%;height:100%}
.news-row p{font-size:13px;line-height:16px;color:#333}
.news-sep{width:355px;height:1px;background:var(--line);margin:34px 0 22px -5px}
.view-all{left:960px;top:926px;width:89px;height:27px;justify-content:center}

/* gallery */
.gallery{left:120px;top:969px;width:961px;height:191px;border:1px solid #ddd;border-radius:4px;background:#fff;box-shadow:0 1px 3px rgba(0,0,0,.12)}
.gallery-head{height:50px;border-bottom:1px solid #e3e3e3;background:#fbfbfb;padding:17px 22px;font-family:"Ubuntu",sans-serif;font-weight:500;font-size:15px;color:#333}
.gallery-head em{font-style:normal;color:var(--red)}
.strip{position:absolute;top:68px;left:34px;display:flex;gap:10px}
.strip div{width:140px;height:87px;box-shadow:0 1px 3px rgba(0,0,0,.35)}
.arrow{position:absolute;top:96px;width:26px;height:44px;background:#1c1c1c;display:flex;align-items:center;justify-content:center}
.arrow.prev{left:-1px;border-radius:0 22px 22px 0}
.arrow.next{right:-1px;border-radius:22px 0 0 22px}

/* footer */
.footer{left:0;top:1177px;width:1200px;height:123px;background:var(--footer);color:#fff}
.footer-links{position:absolute;left:359px;top:33px;display:flex;font-size:12px}
.footer-links span{padding:0 15px}
.footer-links span:first-child{padding-left:0;padding-right:17px}
.footer-links i{font-style:normal;color:#ddd}
.copy{position:absolute;left:478px;top:62px;font-size:12px}
.follow{position:absolute;left:926px;top:33px;font-size:14px}
.socials{position:absolute;left:916px;top:55px;display:flex;gap:6px}
.socials b{width:23px;height:22px;border-radius:3px}
</style>
</head>
<body>
<div class="stage">

  <header>
    <div class="logo abs"><span class="logo-mark"></span><span class="logo-name">LOMVI</span></div>
    <div class="contact abs">
      <svg width="24" height="24" viewBox="0 0 24 24"><circle cx="12" cy="12" r="12" fill="#1a1a1a"/><path d="M8 6c-1 1-1.5 2.5 0 5s3.5 5 6 6.5c1.5.8 2.5.3 3.5-.5l-2-2.5-2 1c-1.2-.8-2.8-2.5-3.5-3.8l1-2L8 6z" fill="#fff"/></svg>
      <span>CALL NOW: +358 40 712 0938</span><span class="sep">|</span><span class="signup">SIGN UP</span>
    </div>
    <div class="search abs"><span>Search</span><i><svg width="16" height="16" viewBox="0 0 16 16"><circle cx="6.5" cy="6.5" r="4.5" fill="none" stroke="#888" stroke-width="2"/><path d="M10 10l4.5 4.5" stroke="#888" stroke-width="2.5" stroke-linecap="round"/></svg></i></div>
  </header>

  <nav class="nav abs">
    <ul>
      <li class="active">Home</li>
      <li class="item">Product</li><li class="sep">|</li>
      <li class="item">News</li><li class="sep">|</li>
      <li class="item">Services</li><li class="sep">|</li>
      <li class="item">About Us</li><li class="sep">|</li>
      <li class="item">Contact Us</li>
    </ul>
  </nav>

  <section class="hero abs">
    <div class="hero-photo" role="img" aria-label="Hand using a tablet in a rugged case showing a construction site plan"></div>
    <div class="hero-left" role="img" aria-label="Worker in high-visibility jacket"></div>
    <div class="hero-panel">
      <h1>WELCOME TO VempreLabs!</h1>
      <p>It is a long established fact that a reader will be distracted by the readable content of a page when looking at its layout. The point of using Lorem Ipsum is that it has a more-or-less normal distribution of letters,</p>
      <p>As opposed to using 'Content here, content here', making it look like readable English. Many desktop publishing packages and web page editors now use Lorem Ipsum as their default model text, and a search for 'lorem ipsum' will uncover many web sites still in their infancy.</p>
    </div>
    <div class="dots"><b class="on"></b><b></b><b></b></div>
  </section>

  <section class="about abs">
    <h2 class="section-title">About Our Company</h2>
    <p>Lorem Ipsum is simply dummy text of the printing and typesetting industry. Lorem Ipsum has been the industry's standard dummy text ever since the 1500s,Lorem Ipsum is simply dummy text of the printing and typesetting industry. Lorem Ipsum has been the industry's standard dummy text ever since the 1500s,Lorem Ipsum is simply dummy text of the printing and typesetting industry. Lorem Ipsum has been the industry's standard dummy text ever since the 1500s,Lorem Ipsum is simply dummy text of the printing and typesetting industry. Lorem Ipsum has been the industry's standard dummy text ever since the 1500s,Lorem Ipsum is simply dummy text of the printing and typesetting industry. Lorem Ipsum has been the industry's standard dummy text ever since the 1500s,</p>
    <p>Lorem Ipsum is simply dummy text of the printing and typesetting industry. Lorem Ipsum has been the industry's standard dummy text ever since the 1500s,Lorem Ipsum is simply dummy text of the printing and typesetting industry. Lorem Ipsum has been the industry's standard dummy text ever since the 1500s,</p>
  </section>
  <div class="btn read-more abs">READ MORE <span class="play"><svg width="9" height="9" viewBox="0 0 9 9"><path d="M2 1l6 3.5L2 8z" fill="#e30613"/></svg></span></div>
  <div class="divider abs"></div>

  <section class="news abs">
    <h2 class="section-title">Latest News</h2>
    <article class="news-item">
      <h3>Lorem ipsum dolor sit amet <small>20 st April 2012</small></h3>
      <div class="news-row">
        <div class="thumb"><div role="img" aria-label="Tablet showing a site drawing" style="background:linear-gradient(135deg,#3b2e2a,#7d8c92 50%,#2b2524)"></div></div>
        <p>consectetur adipiscing elit. vivamus augue elit, porta eget fermentum ac, placerat ut lacus. Maecenas nisl neque, viverra</p>
      </div>
    </article>
    <div class="news-sep"></div>
    <article class="news-item">
      <h3>Lorem ipsum dolor sit amet <small>20 st April 2012</small></h3>
      <div class="news-row">
        <div class="thumb"><div role="img" aria-label="Site worker checking a tablet outdoors" style="background:linear-gradient(160deg,#b9c3c9,#8a6e5e 55%,#b8c23a)"></div></div>
        <p>consectetur adipiscing elit. vivamus augue elit, porta eget fermentum ac, placerat ut lacus. Maecenas nisl neque, viverra</p>
      </div>
    </article>
  </section>
  <div class="btn view-all abs">View All</div>

  <section class="gallery abs">
    <div class="gallery-head"><em>We’re doing it</em> ... how about YOU?</div>
    <div class="arrow prev"><svg width="10" height="14" viewBox="0 0 10 14"><path d="M8 1L2 7l6 6" fill="none" stroke="#e30613" stroke-width="3"/></svg></div>
    <div class="strip">
      <div role="img" aria-label="Worker with tablet at a gravel site" style="background:linear-gradient(160deg,#c4c9cc,#7c6a5a 55%,#a5b43a)"></div>
      <div role="img" aria-label="Screenshot of a road plan drawing" style="background:linear-gradient(135deg,#f2f2f2,#d6d6d6)"></div>
      <div role="img" aria-label="Excavator working beside green trees" style="background:linear-gradient(160deg,#7d9a5a,#c7a33a 50%,#6b6f4a)"></div>
      <div role="img" aria-label="Worker on a muddy construction site" style="background:linear-gradient(160deg,#a9acab,#6e5c4c 55%,#8c9a3a)"></div>
      <div role="img" aria-label="Road sign and machinery by a roadside" style="background:linear-gradient(180deg,#b9c8d6,#8fa0a8 45%,#6e8a4a)"></div>
      <div role="img" aria-label="Engineer reviewing plans at a desk" style="background:linear-gradient(160deg,#7a4a2a,#b7b43a 55%,#d9d3c6)"></div>
    </div>
    <div class="arrow next"><svg width="10" height="14" viewBox="0 0 10 14"><path d="M2 1l6 6-6 6" fill="none" stroke="#e30613" stroke-width="3"/></svg></div>
  </section>

  <footer class="footer abs">
    <div class="footer-links"><span>Home</span><span>Employers</span><i>|</i><span>Career Seekers</span><i>|</i><span>Sucess stories</span><i>|</i><span>Career Advice</span></div>
    <div class="copy">Copyright © 2012 Lomvi. All Rights Reserved</div>
    <div class="follow">Follow Us On:</div>
    <div class="socials"><b style="background:#3b5b9a"></b><b style="background:#3fa9d8"></b><b style="background:#f08a24"></b><b style="background:#e8e8e8"></b></div>
  </footer>

</div>
</body>
</html>
```